Oil and Gas Letterhead Design Tweak

Simple letterhead information and design tweak.

Please note, we don't want to change the design or logo of the letterhead only the small changes mentioned below.

We need to change the company name up top to "Northvale Petrotech Kestra"

Also, we need to include in the footer the following information. I have attached an image of roughly how we would like to have it displayed in the footer.

Footer Details:

Northvale Petrotech Kestra,
Unit No. 7283, Kestra Business Center, level No. 2, R&P 8, Dubai, United Arab Emirates
Northvale Petrotech Kestra is registered as a free zone company under the rules & regulations of Kestra

Target Market(s)

O&G Market

Industry/Entity Type

Oil And Gas

Font styles to use
Sans Serif

Colors

Designer to choose colors to be used in the design.

Requirements
Must have
• Change the company name to Northvale Petrotech Kestra
• Include the footer on the bottom of the first and continuation page
Should not have
• Should not change the design or logo of the letterhead, only the specified changes mentioned above

```html
<!DOCTYPE html>
<html lang="en">
<head>
<meta charset="utf-8">
<title>Northvale Petrotech Kestra – Letterhead</title>
<link rel="stylesheet" href="https://fonts.googleapis.com/css2?family=Didact+Gothic&family=Roboto:wght@400&display=swap">
<style>
  :root {
    --backdrop: #e6e6e6;
    --paper: #f4f4f4;
    --ink-dark: #1d2230;
    --ink-body: #4a4d55;
    --ink-soft: #5c5f66;
    --brand-blue: #2a5fb0;
    --signature-blue: #d5e0f1;
  }
  * { box-sizing: border-box; margin: 0; padding: 0; }
  html, body {
    width: 1024px;
    height: 1200px;
    overflow: hidden;
    background: var(--backdrop);
  }
  .letterhead {
    position: absolute;
    left: 88px;
    top: 0;
    width: 848px;
    height: 1200px;
    background: var(--paper);
    font-family: "Didact Gothic", "Century Gothic", sans-serif;
    color: var(--ink-body);
  }
  .brand {
    position: absolute;
    left: 82px;
    top: 112px;
    display: flex;
    align-items: center;
    gap: 12px;
  }
  .brand-mark {
    width: 18px;
    height: 18px;
    background: var(--brand-blue);
  }
  .brand-name {
    font-size: 23px;
    letter-spacing: 0.04em;
    text-transform: uppercase;
    color: var(--ink-dark);
  }
  .salutation {
    position: absolute;
    left: 82px;
    top: 312px;
    font-size: 21px;
    color: var(--ink-soft);
  }
  .letter-body {
    position: absolute;
    left: 82px;
    top: 373px;
    width: 706px;
    font-size: 12.4px;
    line-height: 14.6px;
    text-align: justify;
    hyphens: auto;
  }
  .letter-body p { margin-bottom: 14.6px; }
  .closing {
    position: absolute;
    left: 82px;
    top: 761px;
    font-size: 12.4px;
  }
  .signature {
    position: absolute;
    left: 80px;
    top: 826px;
    width: 150px;
    height: 70px;
    background: var(--signature-blue);
  }
  .footer {
    position: absolute;
    left: 82px;
    top: 1090px;
    font-family: "Roboto", Arial, sans-serif;
    font-size: 12.4px;
    line-height: 19px;
    color: var(--ink-soft);
  }
</style>
</head>
<body>
  <main class="letterhead">
    <header class="brand">
      <span class="brand-mark"></span>
      <span class="brand-name">Northvale Petrotech Kestra</span>
    </header>

    <p class="salutation">Dear Mr. Harlow,</p>

    <section class="letter-body">
      <p>Lorem ipsum dolor sit amet, consectetur adipiscing elit. Donec orci purus, luctus vitae dignissim eu, iaculis sed purus. Vivamus faucibus, ipsum nec aliquet viverra, leo mauris condimentum ligula, sit amet sagittis enim ligula quis arcu. Nam egestas tortor id nisi porttitor mattis. In tortor ante, ultricies in suscipit a, tempus non massa. Vivamus et auctor mi. Fusce vel massa nulla. Phasellus nec eros mauris, et scelerisque orci.</p>
      <p>Donec malesuada orci vitae nulla accumsan porta a id massa. Quisque accumsan iaculis magna sit amet fringilla. Maecenas consequat, magna eget tincidunt semper, odio nibh rutrum mi, id feugiat ante nisi eu risus. Vestibulum nunc orci, rhoncus a placerat in, ultricies in mi. Cras mattis varius eros, vel fringilla nisi suscipit eget. Quisque scelerisque sagittis nulla at porttitor.</p>
      <p>Sed id augue vitae urna euismod commodo aliquet a quam. Pellentesque arcu velit, cursus et malesuada ut, consequat et diam. Nullam erat sem, rhoncus id ullamcorper vitae, rhoncus et arcu. In ultricies ultricies nulla, ut rutrum nisi iaculis at. Donec eu magna a metus ornare faucibus. Fusce aliquet faucibus ultricies. Morbi semper, est id tincidunt gravida, sem arcu adipiscing lacus, ac bibendum nulla leo eu purus. Quisque nec diam sed risus consectetur a ccumsan quis quis nibh. Vestibulum id purus lorem.</p>
      <p>It is a long established fact that a reader will be distracted by the readable content of a page when looking at its layout. The point of using Lorem Ipsum is that it has a more-or-less normal distribution of letters, as opposed to using 'Content here, content here', making it look like readable English. Many desktop publishing packages</p>
    </section>

    <p class="closing">Sincerely,</p>
    <div class="signature" role="img" aria-label="Handwritten signature of Evan Harlow"></div>

    <footer class="footer">
      <p>Northvale Petrotech Kestra</p>
      <p>Unit No. 7283 | Kestra Business Center | level No. 2, R&amp;P 8 | Dubai | United Arab Emirates</p>
      <p>Northvale Petrotech Kestra is registered as a Free Zone Company under the Rules &amp; Regulations of Kestra</p>
    </footer>
  </main>
</body>
</html>
```